Yoga Training Cerificate

Design a certificate of graduation from a Vinyasa Yoga Teacher Training Program.

The attached document is an example of the certificate I received as a graduate from a teacher training program. You can use it as a template.

Stylistically, what you design can be: visually enticing, professional, clean, and modern.

Please develop the "Tidal Lotus" logo and embed it within the certificate.

Please add a circular watermark behind the body of the certificate similar to the one found in the attachment; leave out the words Asana Guild because I am not associated with that organization.

The name of my school is "Tidal Lotus." And it was established in 2017, which you can include.

The certificate affirms that "' 'such-and-such' has successfully completed the Tidal Lotus modern vinyasa yoga training, completing two hundred hours of instruction in practice and theory. Within the power of our institution as a certifying agent we declare Such-and-such, now, a teacher competent to share the gift of yoga with the masses in a safe and effective."

My name -Dennis Halvorsen- should be at bottom with a faux-signature; position title: Tidal Lotus founder.

If you decide to include text on the fringe, like the example, it might include bars of text describing the maxims of the Tidal Lotus school reading:

This is Tidal Lotus
Breath is primary
Evolve the physical culture
Bring your unique expression to the practice
Take Breaks
Freestyle
Close your eyes
Feel deeper into your body
This is active meditation
This is moving meditation
This is modern meditation

And find a way to integrate Emojis like: Fire, Water, Prayer Hands, etc. as you see fit.

Generally, make the certificate look: official, clear and clean. You can base it from the example given. And try and create a graphic design that is more visually capturing then the example.

```html
<!DOCTYPE html>
<html lang="en">
<head>
<meta charset="utf-8">
<title>Tidal Lotus – Certificate of Completion</title>
<link rel="stylesheet" href="https://fonts.googleapis.com/css2?family=Pinyon+Script&family=Roboto:wght@300;400;700&family=Raleway:wght@300&display=swap">
<style>
  :root {
    --ink: #231f20;
    --paper: #ffffff;
    --seal: #d6d6d6;
  }
  * { margin: 0; padding: 0; box-sizing: border-box; }
  html, body { width: 1200px; height: 849px; overflow: hidden; background: var(--paper); }
  .certificate {
    position: relative;
    width: 1200px;
    height: 849px;
    background: var(--paper);
    color: var(--ink);
    font-family: "Roboto", Arial, sans-serif;
  }
  .frame { position: absolute; inset: 0; }
  .seal { position: absolute; inset: 0; }
  .brand-mark {
    position: absolute;
    left: 0; right: 0;
    top: 118px;
    text-align: center;
    font-family: "Raleway", "Roboto", sans-serif;
    font-weight: 300;
    font-size: 38px;
    color: var(--ink);
    letter-spacing: 0.5px;
  }
  .title {
    position: absolute;
    left: 0; right: 0;
    top: 212px;
    text-align: center;
    font-family: "Pinyon Script", cursive;
    font-size: 70px;
    line-height: 1;
    font-weight: 400;
  }
  .affirm {
    position: absolute;
    left: 0; right: 0;
    top: 318px;
    text-align: center;
    font-weight: 300;
    font-size: 22px;
  }
  .recipient {
    position: absolute;
    left: 0; right: 0;
    top: 362px;
    text-align: center;
    font-weight: 700;
    font-size: 80px;
    line-height: 1.1;
    letter-spacing: 0.5px;
  }
  .statement {
    position: absolute;
    left: 0; right: 0;
    text-align: center;
    font-weight: 300;
    font-size: 21px;
    line-height: 29px;
  }
  .statement strong { font-weight: 700; }
  .statement--course { top: 481px; }
  .statement--declaration { top: 553px; }
  .date {
    position: absolute;
    left: 134px;
    top: 737px;
    font-weight: 700;
    font-size: 21px;
  }
  .signatory {
    position: absolute;
    left: 824px;
    top: 705px;
    width: 242px;
    border-top: 3px solid var(--ink);
    text-align: center;
    padding-top: 6px;
  }
  .signatory__name { font-weight: 700; font-size: 22px; line-height: 26px; }
  .signatory__role { font-weight: 300; font-size: 21px; line-height: 28px; }
</style>
</head>
<body>
<main class="certificate">
  <svg class="seal" width="1200" height="849" aria-hidden="true">
    <circle cx="600" cy="436" r="228" fill="none" stroke="var(--seal)" stroke-width="22"/>
    <circle cx="600" cy="436" r="190" fill="none" stroke="var(--seal)" stroke-width="3"/>
  </svg>

  <svg class="frame" width="1200" height="849" aria-hidden="true">
    <path d="M546 68 H93 V786 H1107 V68 H654" fill="none" stroke="var(--ink)" stroke-width="3.5"/>
    <circle cx="600" cy="62" r="34" fill="none" stroke="var(--ink)" stroke-width="3.5"/>
  </svg>

  <div class="brand-mark">Tidal Lotus</div>

  <h1 class="title">Certificate of Completion</h1>

  <p class="affirm">The certificate affirms that</p>

  <p class="recipient">MARA ELLISON</p>

  <p class="statement statement--course">
    has successfully completed The Tidal Lotus modern vinyasa yoga training<br>
    completing two hundred hours of instruction in practice and theory.
  </p>

  <p class="statement statement--declaration">
    Within the power of our institution as a certifying agent<br>
    we declare <strong>MARA ELLISON</strong>, now, a teacher<br>
    competent to share the gift of yoga with the masses in a safe and effective.
  </p>

  <p class="date">25 / 5 / 2018</p>

  <div class="signatory">
    <p class="signatory__name">DENNIS HALVORSEN</p>
    <p class="signatory__role">TIDAL LOTUS FOUNDER</p>
  </div>
</main>
</body>
</html>
```